Software Company Requires Website

We need a web design for a new mobile software development company based in London named Velquin Solutions.
The design needs to be clean and smooth. Not too flashy, not too boring.
I would like to try the design with some warm colors, and maybe a headline or something highlighted with a strong color. ( logo ? ) The layout should be something like the bellow links, all in one page.

http://brantelo.net/
http://www.kelvory.com/
http://www.work-plover.de/
http://www.tusker.com/
http://www.quildenta.com/us/

Now some of them they seem different from the others, but in each of them there is something that ticks my brain, so it`s up to you to surprise me.

I have uploaded the logo of the company, so you guys can fit that in your design as well.
Updates

Hy everybody This will be the last update for the brief. The company will focus in the beginning for mobile development only, so i would like the website design to be done in a matter that will reflect that. We will develop IOS, Android and Windows applications. We will also require 3 pages: One for the home menu, one for portfolio and one for contact us. The layout should be the same ( one page scroll down ) but the design of the 3 pages different. Please readdress the brief. Hope that i provided enough information for the scope of the project.

I have uploaded the logo that you guys can use. If the logo requires small modifications you can adjust that to suit your idea as long as the logo does not change completely.

Target Market(s)

High End companies that require simplified software solutions.

Industry/Entity Type

It Company

Number of Pages Required

3 page

Requirements
Must have
• One page scroll down layout for 3 pages:
• one for home page, one for portfolio and one for contact us.
• In the portfolio page we would like to have different display options for given examples of applications ( min 3 )

```html
<!DOCTYPE html>
<html lang="en">
<head>
<meta charset="utf-8">
<title>Velquin Solutions</title>
<link href="https://fonts.googleapis.com/css2?family=Open+Sans:wght@300;400;600;700&family=Roboto+Condensed:wght@300;400&family=Arimo:wght@400&display=swap" rel="stylesheet">
<style>
:root{
  --blue:#3a83c8;
  --blue-deep:#1f66b0;
  --blue-line:#9cc0e6;
  --hero-top:#2f80cc;
  --hero-bottom:#1d5fa6;
  --deck:#1a4f8c;
  --nav-bg:#f3f3f3;
  --section-alt:#f4f6f9;
  --text-grey:#8a8a8a;
  --nav-grey:#b5b5b5;
  --dark:#2b2b2b;
  --white:#ffffff;
}
*{margin:0;padding:0;box-sizing:border-box}
html,body{width:719px;height:1200px;overflow:hidden;background:var(--white)}
body{position:relative;font-family:"Open Sans",sans-serif}
.abs{position:absolute}

/* hero */
.hero{left:0;top:0;width:719px;height:354px;overflow:hidden}
.hero-backdrop{left:0;top:0;width:719px;height:354px;background:linear-gradient(180deg,var(--hero-top) 0%,#2a75c2 70%,var(--hero-bottom) 79%,var(--deck) 100%)}
.brand-hero{left:103px;top:40px;color:var(--white);font-family:"Open Sans",sans-serif;font-weight:300;line-height:1}
.brand-hero .name{display:block;font-size:62px;letter-spacing:1px}
.brand-hero .sub{display:block;font-size:17px;letter-spacing:9px;margin-top:8px;padding-left:4px}
.tagline{left:103px;top:160px;color:var(--white);font-weight:300;font-size:16px;line-height:20px;letter-spacing:.2px}
.hero-cta{left:103px;top:225px;height:31px;padding:0 12px;background:rgba(20,60,110,.35);color:var(--white);font-weight:300;font-size:15px;line-height:31px;display:flex;align-items:center;gap:12px}
.scroll-cue{left:105px;top:298px}
.hero-device{left:472px;top:40px;width:192px;height:292px;border-radius:22px;background:linear-gradient(160deg,#f4f6f8 0%,#d9dee4 60%,#b8c1cc 100%)}

/* navigation */
.topnav{left:0;top:354px;width:719px;height:42px;background:var(--nav-bg)}
.brand-small{left:103px;top:13px;color:var(--blue-deep);font-size:13px;font-weight:600}
.menu{right:103px;top:0;height:42px;display:flex;align-items:center;gap:27px;list-style:none;font-size:8px;letter-spacing:.3px}
.menu li{color:var(--nav-grey)}
.menu li.active{color:var(--blue-deep);font-weight:700}

/* section headings */
.section-title{left:0;width:719px;text-align:center;font-family:"Roboto Condensed",sans-serif;font-weight:300;font-size:26px;color:var(--blue);letter-spacing:.5px}
.rule{left:103px;width:513px;height:6px}

/* about */
.about-text{left:120px;width:479px;color:var(--text-grey);font-family:"Arimo",sans-serif;font-size:7.3px;line-height:9.2px;text-align:center}

/* portfolio */
.portfolio{left:0;top:597px;width:719px;height:317px;background:var(--section-alt)}
.grid{left:103px;top:675px;width:513px;height:207px;display:grid;grid-template-columns:repeat(3,1fr);grid-template-rows:repeat(2,1fr)}
.tile{position:relative}
.tile-a{background:radial-gradient(circle at 50% 55%,#f6f6f6,#dedede)}
.tile-b{background:radial-gradient(circle at 55% 60%,#ffffff,#e3e5e8)}
.tile-c{background:radial-gradient(circle at 50% 55%,#f2f2f2,#d8d8d8)}
.tile-d{background:radial-gradient(circle at 50% 55%,#f0f0f0,#d3d3d3)}
.tile-f{background:radial-gradient(circle at 50% 55%,#f4f4f4,#dcdcdc)}
.tile-feature{background:var(--blue);color:var(--white);text-align:center}
.tile-feature .plus{position:absolute;left:72px;top:14px}
.tile-feature h3{position:absolute;left:0;width:100%;top:47px;font-size:11px;font-weight:700;letter-spacing:.3px}
.tile-feature .more{position:absolute;left:50px;top:68px;width:71px;height:17px;background:#dfe9f4;color:var(--blue);font-size:7.5px;font-weight:600;line-height:17px}

/* contact */
.contact{left:0;top:914px;width:719px;height:243px;background:linear-gradient(180deg,#333 0%,var(--dark) 60%,#262626 100%)}
.contact .section-title{color:var(--white)}
.info-bar{left:103px;top:995px;width:513px;height:59px;background:rgba(0,0,0,.35);color:var(--white);font-family:"Arimo",sans-serif;font-size:7.5px}
.info{position:absolute;top:24px;display:flex;align-items:center;gap:7px}
.field{background:var(--white);border-radius:2px;font-size:5.5px;font-weight:700;font-style:italic;color:#222;padding:6px 6px 0;letter-spacing:.2px}
.send{left:492px;top:1092px;width:85px;height:23px;background:#2d7bc4;color:var(--white);font-size:10px;font-weight:700;text-align:center;line-height:23px}

/* footer */
.footer{left:0;top:1157px;width:719px;height:43px;background:var(--white)}
.brand-foot{left:103px;top:8px;color:var(--blue-deep);font-size:12px;font-weight:600}
.copyright{left:103px;top:27px;font-size:7.5px;color:#555}
.socials{left:557px;top:12px;display:flex;gap:6px}
.socials span{width:11px;height:11px;border-radius:50%;background:#c9c9c9}
.socials span:first-child{background:var(--blue-deep)}
.legal{right:103px;top:28px;font-size:7.5px;color:#555}
.legal .sep{margin:0 8px}
</style>
</head>
<body>

<header class="abs hero">
  <div class="abs hero-backdrop" role="img" aria-label="Blue textured wall above a blue wooden deck"></div>
  <div class="abs brand-hero"><span class="name">VELQUIN</span><span class="sub">SOLUTIONS</span></div>
  <p class="abs tagline">MOBILE SOFTWARE DEVELOPMENT COMPANY<br>BASED IN LONDON.</p>
  <div class="abs hero-cta">CONTACT VELQUIN
    <svg width="13" height="13" viewBox="0 0 13 13"><path d="M6.5 0v13M0 6.5h13" stroke="#fff" stroke-width="1.3"/></svg>
  </div>
  <svg class="abs scroll-cue" width="28" height="14" viewBox="0 0 28 14"><path d="M1 2l13 10L27 2" fill="none" stroke="#fff" stroke-width="1.6"/></svg>
  <div class="abs hero-device" role="img" aria-label="White smartphone unzipping with colourful app icons flying out"></div>
</header>

<nav class="abs topnav">
  <div class="abs brand-small">Velquin</div>
  <ul class="abs menu">
    <li class="active">HOME</li>
    <li>PORTFOLIO</li>
    <li>CONTACT US</li>
  </ul>
</nav>

<section class="about">
  <h2 class="abs section-title" style="top:420px">ABOUT</h2>
  <svg class="abs rule" style="top:451px" viewBox="0 0 513 6"><path d="M0 .5h513" stroke="#4a8fd4"/><path d="M0 3h513" stroke="#9cc0e6"/><path d="M245 3h23l-11.5 3z" fill="#4a8fd4"/></svg>
  <p class="abs about-text" style="top:469px">Lorem ipsum dolor sit amet, consectetuer adipiscing elit, sed diam nonummy nibh euismod tincidunt ut laoreet dolore magna aliquam erat volutpat. Ut wisi enim ad minim veniam, quis nostrud exerci tation ullamcorper suscipit lobortis nisl ut aliquip ex ea commodo consequat. Duis autem vel eum iriure dolor in hendrerit in vulputate velit esse molestie consequat, vel illum dolore eu feugiat nulla facilisis at vero eros et accumsan et iusto odio dignissim qui blandit praesent luptatum zzril delenit augue duis dolore te feugait nulla facilisi.</p>
  <p class="abs about-text" style="top:522px">Ut wisi enim ad minim veniam, quis nostrud exerci tation ullamcorper suscipit lobortis nisl ut aliquip ex ea commodo consequat. Duis autem vel eum iriure dolor in hendrerit in vulputate velit esse molestie consequat, vel illum dolore eu feugiat nulla facilisis at vero eros et accumsan et iusto odio dignissim qui blandit praesent luptatum zzril delenit augue duis dolore te feugait nulla facilisi.</p>
</section>

<section class="abs portfolio"></section>
<h2 class="abs section-title" style="top:622px">PORTFOLIO</h2>
<svg class="abs rule" style="top:654px" viewBox="0 0 513 6"><path d="M0 .5h513" stroke="#4a8fd4"/><path d="M0 3h513" stroke="#9cc0e6"/><path d="M245 3h23l-11.5 3z" fill="#4a8fd4"/></svg>
<div class="abs grid">
  <div class="tile tile-a" role="img" aria-label="Smartphone surrounded by a ring of app icons"></div>
  <div class="tile tile-b" role="img" aria-label="Smartphone with app icons scattering into the air"></div>
  <div class="tile tile-c" role="img" aria-label="Curved wooden bookshelf filled with colourful books"></div>
  <div class="tile tile-d" role="img" aria-label="Laptop with an online shop scene on its screen"></div>
  <div class="tile tile-feature">
    <svg class="plus" width="27" height="27" viewBox="0 0 27 27"><path d="M13.5 0v27M0 13.5h27" stroke="#fff" stroke-width="1.2"/></svg>
    <h3>LOREM IPSUM DOLOR</h3>
    <div class="more">READ MORE</div>
  </div>
  <div class="tile tile-f" role="img" aria-label="Smartphone surrounded by a ring of app icons"></div>
</div>

<section class="abs contact" role="img" aria-label="Dark street map of London and surrounding towns"></section>
<h2 class="abs section-title" style="top:942px;color:#fff">CONTACT US</h2>
<svg class="abs rule" style="top:974px" viewBox="0 0 513 6"><path d="M0 .5h513" stroke="#ffffff"/><path d="M0 3h513" stroke="#9a9a9a"/><path d="M245 3h23l-11.5 3z" fill="#ffffff"/></svg>
<div class="abs info-bar">
  <div class="info" style="left:40px">
    <svg width="9" height="9" viewBox="0 0 10 10"><path d="M2 0.5l2 2.2-1 1.2c.6 1.3 1.6 2.3 2.9 2.9l1.2-1 2.2 2-1.2 1.7C4.3 9.5.5 5.7.3 1.7z" fill="#fff"/></svg>
    <span>11 22 38 46 57</span>
  </div>
  <div class="info" style="left:204px">
    <svg width="10" height="10" viewBox="0 0 10 10"><path d="M5 0v10M0 5h10M1.5 1.5l7 7M8.5 1.5l-7 7" stroke="#fff" stroke-width="1.3"/></svg>
    <span>123 , Address ABC, LONDON</span>
  </div>
  <div class="info" style="left:380px">
    <svg width="10" height="8" viewBox="0 0 10 8"><rect x=".5" y=".5" width="9" height="7" fill="none" stroke="#fff"/><path d="M.5 .5L5 4.5 9.5 .5" fill="none" stroke="#fff"/></svg>
    <span>info@velquinsolutions.com</span>
  </div>
</div>
<form>
  <div class="abs field" style="left:103px;top:1069px;width:139px;height:20px">NAME</div>
  <div class="abs field" style="left:103px;top:1092px;width:139px;height:20px">TELEPHONE</div>
  <div class="abs field" style="left:103px;top:1115px;width:139px;height:20px">EMAIL</div>
  <div class="abs field" style="left:273px;top:1069px;width:172px;height:66px">MESSAGE</div>
  <div class="abs send">SEND</div>
</form>

<footer class="abs footer">
  <div class="abs brand-foot">Velquin</div>
  <div class="abs copyright">© VELQUIN SOLUTIONS 2014</div>
  <div class="abs socials"><span></span><span></span><span></span><span></span></div>
  <div class="abs legal">Terms &amp; Conditions<span class="sep">|</span>Site map</div>
</footer>

</body>
</html>
```